Visitenkarten-Design für junges Internetportal
Zielgruppe
Wir vertreiben Freizeitangebote für Kinder. Wir haben unter dem Suchbegriff 'spaßlotsen' ein Erklärvideo bei YouTube. Die Visitenkarte ist zur Gewinnung unserer Partner bestimmt, wie z.B. Sportvereine, Tanzschule, Kreativschulen usw....
Aufgabenstellung
Meine Vorstellung ist eine schlichte Karte.

```html
<!DOCTYPE html>
<html lang="de">
<head>
<meta charset="utf-8">
<title>spaßlotsen – Visitenkarte</title>
<link rel="stylesheet" href="https://fonts.googleapis.com/css2?family=Comfortaa:wght@500&family=Oswald:wght@400;500&display=swap">
<style>
  :root {
    --page: #ebe7e2;
    --card: #ffffff;
    --navy: #2f3a4f;
    --teal: #3dbca8;
    --pink-soft: #f6d3da;
    --mint-soft: #d6f0ec;
    --grey-soft: #e4e4e6;
    --shadow: rgba(40, 40, 50, 0.18);
  }
  * { box-sizing: border-box; margin: 0; padding: 0; }
  html, body {
    width: 1200px;
    height: 891px;
    overflow: hidden;
    background: var(--page);
  }
  .stage {
    width: 1200px;
    height: 891px;
    display: flex;
    align-items: center;
    justify-content: center;
    gap: 60px;
  }
  .card {
    position: relative;
    width: 520px;
    height: 300px;
    background: var(--card);
    border-radius: 4px;
    box-shadow: 0 10px 30px var(--shadow);
    overflow: hidden;
  }
  .card__pattern {
    position: absolute;
    inset: 0;
    background:
      radial-gradient(circle at 8% 18%, var(--pink-soft) 0, transparent 22%),
      radial-gradient(circle at 92% 22%, var(--mint-soft) 0, transparent 22%),
      radial-gradient(circle at 12% 88%, var(--grey-soft) 0, transparent 20%),
      radial-gradient(circle at 88% 90%, var(--pink-soft) 0, transparent 22%),
      var(--card);
  }
  .brand {
    position: absolute;
    left: 0;
    right: 0;
    text-align: center;
  }
  .brand__mark {
    display: block;
    width: 70px;
    height: 70px;
    margin: 0 auto 14px;
    border-radius: 50%;
    background: var(--teal);
  }
  .brand__name {
    font-family: "Comfortaa", sans-serif;
    font-weight: 500;
    font-size: 40px;
    letter-spacing: 1px;
    color: var(--navy);
    line-height: 1;
  }
  .brand__url {
    margin-top: 10px;
    font-family: "Oswald", sans-serif;
    font-weight: 500;
    font-size: 19px;
    color: var(--teal);
    letter-spacing: 0.3px;
  }
  .card--front .brand { top: 58px; }
  .card--back .brand { top: 34px; }
  .card--back .brand__mark { width: 56px; height: 56px; margin-bottom: 12px; }
  .card--back .brand__name { font-size: 34px; }
  .contact-bar {
    position: absolute;
    left: 0;
    right: 0;
    bottom: 0;
    height: 72px;
    background: var(--navy);
    display: flex;
    align-items: center;
    justify-content: space-around;
    padding: 0 14px;
  }
  .contact {
    display: flex;
    align-items: center;
    gap: 8px;
    font-family: "Oswald", sans-serif;
    font-weight: 400;
    font-size: 15px;
    color: #ffffff;
    letter-spacing: 0.3px;
  }
  .contact__icon {
    width: 26px;
    height: 26px;
    border-radius: 50%;
    background: var(--teal);
    display: flex;
    align-items: center;
    justify-content: center;
    flex: none;
  }
</style>
</head>
<body>
  <main class="stage">
    <section class="card card--front" aria-label="Vorderseite">
      <div class="card__pattern" role="img" aria-label="Dekoratives Muster aus stilisierten Vogelköpfen in Rosa, Mint und Grau"></div>
      <div class="brand">
        <span class="brand__mark"></span>
        <p class="brand__name">spaßlotsen</p>
        <p class="brand__url">www.spasslotsen.de</p>
      </div>
    </section>

    <section class="card card--back" aria-label="Rückseite">
      <div class="card__pattern" role="img" aria-label="Dekoratives Muster aus stilisierten Vogelköpfen in Rosa, Mint und Grau"></div>
      <div class="brand">
        <span class="brand__mark"></span>
        <p class="brand__name">spaßlotsen</p>
        <p class="brand__url">www.spasslotsen.de</p>
      </div>
      <div class="contact-bar">
        <p class="contact">
          <span class="contact__icon">
            <svg width="14" height="14" viewBox="0 0 24 24" aria-hidden="true"><path fill="#fff" d="M6.6 10.8a15 15 0 0 0 6.6 6.6l2.2-2.2c.3-.3.7-.4 1-.2 1.1.4 2.3.6 3.6.6.6 0 1 .4 1 1V20c0 .6-.4 1-1 1A17 17 0 0 1 3 4c0-.6.4-1 1-1h3.5c.6 0 1 .4 1 1 0 1.3.2 2.5.6 3.6.1.3 0 .7-.2 1z"/></svg>
          </span>
          02041 7382915
        </p>
        <p class="contact">
          <span class="contact__icon">
            <svg width="14" height="14" viewBox="0 0 24 24" aria-hidden="true"><rect x="3" y="6" width="18" height="12" rx="1.5" fill="#fff"/><path d="M3.5 6.8 12 13l8.5-6.2" fill="none" stroke="#3dbca8" stroke-width="1.6"/></svg>
          </span>
          post@spasslotsen.de
        </p>
        <p class="contact">
          <span class="contact__icon"></span>
          Profil: spaßlotsen
        </p>
      </div>
    </section>
  </main>
</body>
</html>
```